Poster - to Promote Study Skills

I have written a book about study skills for students. I want to move to using the book to give presentations. This poster looks to emphasise the fact that time is not the most important element of creating study impact, it is the intensity of the effort. The steps outline the increasing effectiveness of a study effort. The highest steps are the most effective. I have done a very rough design. It was written in the excel document, and there is a screen shot of it in the word document. I have done it is landscape, however I think it might be more effective in a portrait format.

Target Market(s)

Students aged 13 to 21

Requirements
Must have
• The 'steps' included in the files
Nice to have
• Would like to have design features, maybe colours, that support the fact that the higher 'study steps' are better.

```html
<!DOCTYPE html>
<html lang="en">
<head>
<meta charset="utf-8">
<title>Your Study Impact = Intensity of Effort x Time</title>
<link href="https://fonts.googleapis.com/css2?family=Open+Sans:ital,wght@0,400;0,600;0,700;0,800;1,400;1,600&display=swap" rel="stylesheet">
<style>
  :root {
    --page: #f7f7f4;
    --panel: #e9ece6;
    --panel-edge: #cfd6c8;
    --ink: #2b2f2b;
    --muted: #4a4f4a;
    --step60-dark: #1f6b2c; --step60: #2f8a3c;
    --step50-dark: #3a8a2e; --step50: #55a33f;
    --step40-dark: #5d9e33; --step40: #78b54a;
    --step30-dark: #3c9a6a; --step30: #5bb384;
    --step20-dark: #2f9a98; --step20: #4fb3b0;
    --step10-dark: #2d7fbf; --step10: #4a9ad6;
    --on-step: #ffffff;
  }
  * { box-sizing: border-box; margin: 0; padding: 0; }
  html, body { width: 849px; height: 1200px; overflow: hidden; }
  body {
    background: var(--page);
    font-family: "Open Sans", Arial, sans-serif;
    color: var(--ink);
    position: relative;
  }
  .poster {
    position: absolute;
    left: 65px; top: 62px;
    width: 720px; height: 1098px;
    background: linear-gradient(180deg, #e4ebdf 0%, var(--panel) 30%, var(--panel) 100%);
    border: 1px solid var(--panel-edge);
    padding: 22px 0 0;
  }
  .title {
    text-align: center;
    font-size: 27px;
    font-weight: 800;
    letter-spacing: -0.3px;
    line-height: 1.2;
  }
  .subtitle {
    text-align: center;
    font-size: 17px;
    font-style: italic;
    font-weight: 600;
    margin-top: 6px;
    color: var(--muted);
  }
  .step {
    position: absolute;
    left: 43px;
    width: 642px;
    display: flex;
    color: var(--on-step);
  }
  .step-label {
    width: 186px;
    padding: 8px 8px;
    display: flex;
    flex-direction: column;
    justify-content: center;
    align-items: center;
    text-align: center;
  }
  .step-rate { font-size: 10px; font-weight: 600; line-height: 1.2; white-space: nowrap; }
  .step-rate b { font-size: 22px; font-weight: 800; margin-right: 4px; vertical-align: -2px; }
  .step-name { font-size: 15px; font-weight: 800; margin-top: 4px; white-space: nowrap; }
  .step-detail {
    flex: 1;
    padding: 8px 14px;
    font-size: 12.5px;
    line-height: 1.4;
    display: flex;
    align-items: center;
  }
  .step-60 { top: 113px; height: 94px; }
  .step-60 .step-label { background: var(--step60-dark); }
  .step-60 .step-detail { background: var(--step60); }
  .step-50 { top: 306px; height: 85px; }
  .step-50 .step-label { background: var(--step50-dark); }
  .step-50 .step-detail { background: var(--step50); }
  .step-40 { top: 442px; height: 96px; }
  .step-40 .step-label { background: var(--step40-dark); }
  .step-40 .step-detail { background: var(--step40); }
  .step-30 { top: 609px; height: 99px; }
  .step-30 .step-label { background: var(--step30-dark); }
  .step-30 .step-detail { background: var(--step30); }
  .step-20 { top: 736px; height: 102px; }
  .step-20 .step-label { background: var(--step20-dark); }
  .step-20 .step-detail { background: var(--step20); }
  .step-10 { top: 900px; height: 91px; }
  .step-10 .step-label { background: var(--step10-dark); }
  .step-10 .step-detail { background: var(--step10); }
  .quote {
    position: absolute;
    left: 40px; width: 640px;
    text-align: center;
    font-style: italic;
    font-size: 13.5px;
    line-height: 1.5;
    color: var(--muted);
  }
  .quote cite { font-style: normal; font-size: 11.5px; }
  .quote-habit { top: 222px; }
  .quote-focus { top: 550px; }
  .quote-commit { top: 852px; }
</style>
</head>
<body>
  <main class="poster">
    <h1 class="title">Your Study Impact = Intensity of Effort x Time</h1>
    <p class="subtitle">The Formula for Banking High Performance Study Impacts</p>

    <section class="step step-60">
      <div class="step-label">
        <div class="step-rate"><b>$60</b>an Hour Study Effort</div>
        <div class="step-name">The Aspirational Step</div>
      </div>
      <p class="step-detail">Flow – “in the zone” – easy, productive study.<br>Purpose, intent, focus, stress control, positive mindset</p>
    </section>

    <p class="quote quote-habit">“Small things done well every single day slowly become the person you are.”<br><cite>– Mara Ellison, Writer and Educator</cite></p>

    <section class="step step-50">
      <div class="step-label">
        <div class="step-rate"><b>$50</b>an Hour Study Effort</div>
        <div class="step-name">Balance and Health</div>
      </div>
      <p class="step-detail">Study is supported by positive social, recreational and health habits – balance in life. Exercise and healthy eating and community engagement</p>
    </section>

    <section class="step step-40">
      <div class="step-label">
        <div class="step-rate"><b>$40</b>an Hour Study Effort</div>
        <div class="step-name">Studying Smarter</div>
      </div>
      <p class="step-detail">Using effective study techniques – graphic organisers, practise questions, reflecting on study progress, hand writing notes, short, sharp, distraction free periods of effort (pomodoro method), learning from feedback, spaced revision</p>
    </section>

    <p class="quote quote-focus">“Every result you want is built from two things: attention and effort,<br>and both of them are yours to choose.” <cite>– Jonah Reyes</cite></p>

    <section class="step step-30">
      <div class="step-label">
        <div class="step-rate"><b>$30</b>an Hour Study Effort</div>
        <div class="step-name">Right State of Mind</div>
      </div>
      <p class="step-detail">Positive mindset towards the learning (self-directed, setting goals, enthusiastic about challenge). Planning of assignment efforts/revising between learning and the exam – moving away from relying on the last minute and challenging procrastination. Adequate sleep with good sleep habits</p>
    </section>

    <section class="step step-20">
      <div class="step-label">
        <div class="step-rate"><b>$20</b>an Hour Study Effort</div>
        <div class="step-name">Single Tasking</div>
      </div>
      <p class="step-detail">The study environment is free of distractions (quiet, no phone, no TV, non social media, no email, no music with lyrics) with good organisation (eg effective homework diary use)</p>
    </section>

    <p class="quote quote-commit">“Commitment has only two settings. You either give it everything or you don’t.<br>Halfway is not a place you can stay.” <cite>– Grace Whitfield, Harbour City Hoops Coach</cite></p>

    <section class="step step-10">
      <div class="step-label">
        <div class="step-rate"><b>$10</b>an Hour Study Effort</div>
        <div class="step-name">Building a Foundation</div>
      </div>
      <p class="step-detail">Study time is supported by engagement in class</p>
    </section>
  </main>
</body>
</html>
```